Automotive Business Card Design

I would just like a automotive themed card. nothing too extravagant, but catchy.

needs to say something about doing roadside assistance,mobile repairs, Diesel repairs, and Fleet maintenance

it can be single sided or double sided. no preference there.

Industry/Entity Type

Automotive

Contact Information for Business Card

Dana Whitcombe
phone 547 391 2084
Name: Brightway Automotive & Diesel Repair

```html
<!DOCTYPE html>
<html lang="en">
<head>
<meta charset="utf-8">
<title>Brightway Automotive &amp; Diesel Repair – Business Card</title>
<link rel="stylesheet" href="https://fonts.googleapis.com/css2?family=Cinzel:wght@600;700&family=Tinos:wght@400;700&display=swap">
<style>
  :root {
    --bg: #e9e6e1;
    --card: #ffffff;
    --ink-blue: #2f3b98;
    --band: rgba(236, 238, 244, 0.88);
    --engine-light: #8a8d91;
    --engine-mid: #55585c;
    --engine-dark: #24262a;
    --phone-light: #e4ddd6;
    --phone-mid: #cfb3a6;
    --phone-deep: #a98676;
    --shop-light: #b9bcc2;
    --shop-dark: #232529;
    --shop-blue: #2c4a76;
    --shop-navy: #1d2f4d;
  }
  html, body {
    margin: 0;
    padding: 0;
    width: 1200px;
    height: 1037px;
    overflow: hidden;
    background: var(--bg);
  }
  .sheet {
    position: relative;
    width: 1200px;
    height: 1037px;
  }
  .card {
    position: absolute;
    left: 240px;
    width: 720px;
    height: 412px;
    background: var(--card);
    overflow: hidden;
    box-shadow: 0 10px 26px rgba(0, 0, 0, 0.22);
  }
  .card--services { top: 70px; }
  .card--front { top: 550px; }

  /* Services side */
  .services-photos {
    position: absolute;
    top: 0;
    left: 0;
    width: 720px;
    height: 262px;
    display: block;
  }
  .services-band {
    position: absolute;
    left: 0;
    right: 0;
    bottom: 0;
    height: 150px;
    display: flex;
    align-items: center;
    padding-left: 92px;
    border-top: 1px solid #d9dbe2;
  }
  .services-title {
    font-family: "Cinzel", serif;
    font-weight: 700;
    font-size: 46px;
    color: var(--ink-blue);
    letter-spacing: 1px;
    margin: 0;
  }
  .services-divider {
    width: 2px;
    height: 84px;
    background: var(--ink-blue);
    margin: 0 28px 0 30px;
  }
  .services-list {
    list-style: none;
    margin: 0;
    padding: 0;
    font-family: "Tinos", serif;
    font-size: 21px;
    line-height: 23px;
    color: var(--ink-blue);
  }

  /* Front side */
  .front-photo {
    position: absolute;
    top: 0;
    left: 0;
    width: 720px;
    height: 412px;
    display: block;
  }
  .front-band-top {
    position: absolute;
    left: 0;
    right: 0;
    top: 18px;
    height: 58px;
    background: var(--band);
    display: flex;
    align-items: center;
    justify-content: center;
  }
  .company-name {
    font-family: "Cinzel", serif;
    font-weight: 700;
    font-size: 26px;
    color: var(--ink-blue);
    letter-spacing: 0.5px;
    margin: 0;
  }
  .front-band-bottom {
    position: absolute;
    left: 0;
    right: 0;
    bottom: 0;
    height: 150px;
    background: var(--band);
    padding: 26px 0 0 150px;
    box-sizing: border-box;
  }
  .person-name {
    font-family: "Tinos", serif;
    font-weight: 700;
    font-size: 46px;
    letter-spacing: 5px;
    color: var(--ink-blue);
    margin: 0;
    line-height: 1;
  }
  .person-phone {
    font-family: "Tinos", serif;
    font-weight: 700;
    font-size: 30px;
    letter-spacing: 3px;
    color: var(--ink-blue);
    margin: 8px 0 0 20px;
  }
</style>
</head>
<body>
<main class="sheet">

  <section class="card card--services">
    <svg class="services-photos" viewBox="0 0 720 262" role="img" aria-label="Photos: a mechanic's hand with a wrench over an engine, and hands repairing a mobile phone circuit board">
      <defs>
        <linearGradient id="engineTone" x1="0" y1="0" x2="1" y2="1">
          <stop offset="0" stop-color="var(--engine-light)"/>
          <stop offset="0.45" stop-color="var(--engine-mid)"/>
          <stop offset="1" stop-color="var(--engine-dark)"/>
        </linearGradient>
        <linearGradient id="phoneTone" x1="0" y1="0" x2="1" y2="1">
          <stop offset="0" stop-color="var(--phone-light)"/>
          <stop offset="0.55" stop-color="var(--phone-mid)"/>
          <stop offset="1" stop-color="var(--phone-deep)"/>
        </linearGradient>
      </defs>
      <polygon points="0,0 372,0 428,262 0,262" fill="url(#engineTone)"/>
      <polygon points="372,0 720,0 720,262 428,262" fill="url(#phoneTone)"/>
      <line x1="372" y1="0" x2="428" y2="262" stroke="#ffffff" stroke-width="4"/>
    </svg>
    <div class="services-band">
      <h2 class="services-title">SERVICES</h2>
      <span class="services-divider"></span>
      <ul class="services-list">
        <li>Roadside assistance</li>
        <li>Mobile repairs</li>
        <li>Diesel repairs</li>
        <li>And Fleet maintenance</li>
      </ul>
    </div>
  </section>

  <section class="card card--front">
    <svg class="front-photo" viewBox="0 0 720 412" role="img" aria-label="Photo: a smiling mechanic in a blue work shirt working underneath a vehicle">
      <defs>
        <linearGradient id="shopTone" x1="0" y1="1" x2="1" y2="0">
          <stop offset="0" stop-color="var(--shop-light)"/>
          <stop offset="0.3" stop-color="var(--shop-dark)"/>
          <stop offset="0.65" stop-color="var(--shop-blue)"/>
          <stop offset="1" stop-color="var(--shop-navy)"/>
        </linearGradient>
      </defs>
      <rect width="720" height="412" fill="url(#shopTone)"/>
    </svg>
    <div class="front-band-top">
      <h1 class="company-name">BRIGHTWAY AUTOMOTIVE &amp; DIESEL REPAIR</h1>
    </div>
    <div class="front-band-bottom">
      <p class="person-name">Dana Whitcombe</p>
      <p class="person-phone">547 391 2084</p>
    </div>
  </section>

</main>
</body>
</html>
```